【 概要 】 インスタ広告のバナーの制作依頼です。 サイズは1080x1080px 弊社のLPです。https://petgoods.shiranuiworkscollegeacad.net/ このLPを活かすバナーをお願いします。 【文言】 ペット好きのあなたがオリジナルブランドを作って ペット用品開発億万長者に アイデアを簡単に商品化!難しいことは○○にお任せ!自分の好きを仕事にできる! 無料オンライン説明会開催中 【注意事項】 ・画像の著作権は当方に譲渡されるものとします。 ・他媒体への流用を禁止します。 ・如何なる場合でも当方の画像や情報の漏洩は許されません。 ・納品後の画像の再利用は禁止です。 |
どの案も素敵でしたがこちらを採用させて頂きます。
皆様ご提案ありがとうございました。どれも個性的で良い提案ばかりでした。また機会があれば依頼させて頂きますので宜しくお願い致します。

```html
<!DOCTYPE html>
<html lang="ja">
<head>
<meta charset="UTF-8">
<title>ペット用品開発 説明会バナー</title>
<link rel="stylesheet" href="https://fonts.googleapis.com/css2?family=Noto+Sans+JP:wght@500;700;900&display=swap">
<style>
  :root {
    --orange: #d58a45;
    --orange-light: #e0a262;
    --brown-dark: #4a2a18;
    --brown-stroke: #5a3420;
    --gold: #c99a4a;
    --accent-red: #d2502a;
    --accent-orange: #d9782c;
    --text-dark: #3a2a20;
    --white: #ffffff;
    --photo-wall: #e9e4de;
    --photo-mid: #c9b9a6;
    --photo-floor: #8a5e3c;
  }
  html, body {
    margin: 0;
    padding: 0;
    width: 1200px;
    height: 1200px;
    overflow: hidden;
    background: var(--white);
  }
  .banner {
    position: relative;
    width: 1200px;
    height: 1200px;
    overflow: hidden;
    font-family: "Noto Sans JP", sans-serif;
  }
  .photo {
    position: absolute;
    left: 0;
    top: 200px;
    width: 1200px;
    height: 860px;
    background: linear-gradient(180deg, var(--photo-wall) 0%, #ddd3c8 45%, var(--photo-mid) 70%, var(--photo-floor) 100%);
  }
  .top-band {
    position: absolute;
    left: 0;
    top: 0;
    width: 1200px;
    height: 300px;
  }
  .lead {
    position: absolute;
    left: 90px;
    top: 28px;
    margin: 0;
    color: var(--white);
    font-weight: 700;
    font-size: 50px;
    letter-spacing: 2px;
  }
  .headline {
    position: absolute;
    left: 80px;
    top: 108px;
    margin: 0;
    color: var(--white);
    font-weight: 900;
    font-size: 82px;
    letter-spacing: 1px;
    white-space: nowrap;
  }
  .headline .small { font-size: 52px; font-weight: 700; }
  .brush {
    position: absolute;
    left: 0;
    top: 250px;
    width: 520px;
    height: 120px;
  }
  .category {
    position: absolute;
    left: 100px;
    top: 278px;
    margin: 0;
    color: var(--white);
    font-weight: 900;
    font-size: 50px;
    letter-spacing: 2px;
  }
  .title {
    position: absolute;
    left: 490px;
    top: 228px;
    margin: 0;
    color: var(--brown-dark);
    font-weight: 900;
    font-size: 132px;
    letter-spacing: 4px;
    line-height: 1.1;
    -webkit-text-stroke: 10px var(--white);
    paint-order: stroke fill;
    white-space: nowrap;
  }
  .title .ni { font-size: 58px; letter-spacing: 0; }
  .point {
    position: absolute;
    top: 755px;
    width: 330px;
    height: 330px;
    border-radius: 50%;
    background: rgba(255,255,255,0.96);
    box-shadow: 0 6px 20px rgba(0,0,0,0.15);
    display: flex;
    flex-direction: column;
    justify-content: center;
    align-items: center;
    text-align: center;
    color: var(--text-dark);
    font-weight: 700;
    font-size: 40px;
    line-height: 1.6;
  }
  .point--idea { left: 80px; }
  .point--support { left: 435px; }
  .point--passion { left: 790px; }
  .point .em-red { color: var(--accent-red); font-size: 50px; font-weight: 900; }
  .point .em-orange { color: var(--accent-orange); font-size: 50px; font-weight: 900; }
  .cta-bar {
    position: absolute;
    left: 0;
    bottom: 0;
    width: 1200px;
    height: 140px;
    background: var(--orange);
    display: flex;
    align-items: center;
    justify-content: center;
    color: var(--white);
    font-weight: 700;
    font-size: 44px;
    letter-spacing: 3px;
  }
  .cta-bar .arrow { margin-left: 30px; letter-spacing: -4px; }
</style>
</head>
<body>
<div class="banner">
  <div class="photo" role="img" aria-label="室内で並ぶ茶白の猫と黒茶のポメラニアンの写真"></div>

  <svg class="top-band" viewBox="0 0 1200 300" aria-hidden="true">
    <defs>
      <linearGradient id="bandFill" x1="0" y1="0" x2="1" y2="0">
        <stop offset="0" stop-color="#d0843f"/>
        <stop offset="1" stop-color="#e0a262"/>
      </linearGradient>
    </defs>
    <path d="M0 0 H1200 V200 C1000 240 820 280 560 272 C340 265 160 240 0 250 Z" fill="url(#bandFill)"/>
  </svg>

  <p class="lead">ペット好きのあなたが</p>
  <p class="headline">オリジナルブランド<span class="small">を作って</span></p>

  <svg class="brush" viewBox="0 0 520 120" aria-hidden="true">
    <path d="M0 14 L500 6 L515 40 L505 80 L512 112 L0 112 Z" fill="var(--brown-stroke)"/>
    <path d="M0 104 L505 100 L512 114 L0 118 Z" fill="var(--gold)"/>
  </svg>
  <p class="category">ペット用品開発</p>
  <h1 class="title">億万長者<span class="ni">に</span></h1>

  <div class="point point--idea">
    <span>アイデア<span style="font-size:36px">を</span></span>
    <span>簡単に<span class="em-red">商品化!</span></span>
  </div>
  <div class="point point--support">
    <span>難しいことは</span>
    <span>○○に<span class="em-red">お任せ!</span></span>
  </div>
  <div class="point point--passion">
    <span>自分の<span class="em-orange">好き</span>を</span>
    <span>仕事にできる!</span>
  </div>

  <div class="cta-bar">無料オンライン説明会開催中<span class="arrow">&gt;&gt;</span></div>
</div>
</body>
</html>
```